BrivoPeak Business Card Design Project

We are looking for a modern, clean business card design for our new company. We are a consulting firm focused on the financial services market providing management and IT consulting to banks, insurance companies, etc. Please include our company logo and company contact information from the attached file in the design. Two versions of the logo are attached, either version is acceptable. Logos are available in other file formats if needed. We would like to include the contact information for both our UK and US offices as well as the following information for each individual card holder: Name, position/title, address, phone number and e-mail address.
Updates
Project Deadline Extended
Reason: A last minute trip over seas has prevented us from finalizing the decision. A decision will be made this week. We apologize for the inconvenience.
Industry/Entity Type
Business
Contact Information for Business Card
Company logo.
Company locations and phone numbers for both the US and UK offices.
Company URL.
Cardholder Name
Cardholder Position/title
Cardholder Address
Cardholder Phone Number
Cardholder e-mail Address
Look and feel
Each slider illustrates characteristics of the customer's brand and the style your logo design should communicate.

```html
<!DOCTYPE html>
<html lang="en">
<head>
<meta charset="utf-8">
<title>BrivoPeak Partners – Business Card</title>
<link rel="stylesheet" href="https://fonts.googleapis.com/css2?family=Arimo:wght@400;700&display=swap">
<style>
  :root {
    --backdrop: #3a332f;
    --card: #1b1b1c;
    --card-edge: #111112;
    --silver: #a9a9ab;
    --brand-blue: #2b4a7e;
    --ink: #ffffff;
    --muted: #8a8a8c;
  }
  * { margin: 0; padding: 0; box-sizing: border-box; }
  html, body { width: 1200px; height: 780px; overflow: hidden; }
  body {
    background: var(--backdrop);
    font-family: "Arimo", Arial, sans-serif;
    position: relative;
  }
  .card {
    position: absolute;
    width: 525px;
    height: 300px;
    background: var(--card);
    border: 1px solid var(--card-edge);
    box-shadow: 0 10px 28px rgba(0,0,0,.45);
  }
  .card--front { left: 50px; top: 240px; }
  .card--back  { left: 625px; top: 240px; }

  /* Front */
  .front-brand {
    position: absolute; inset: 0;
    display: flex; align-items: center; justify-content: center; gap: 14px;
  }
  .front-brand .mark-square {
    width: 22px; height: 22px; background: var(--silver);
  }
  .front-brand .wordmark {
    font-weight: 700; font-size: 44px; color: var(--silver); letter-spacing: .5px;
  }

  /* Back */
  .back-brand {
    position: absolute; left: 36px; top: 34px;
    display: flex; align-items: center; gap: 12px;
  }
  .back-brand .mark-square { width: 18px; height: 18px; background: var(--brand-blue); }
  .back-brand .wordmark { font-weight: 700; font-size: 34px; color: var(--brand-blue); }

  .divider-left {
    position: absolute; left: 0; top: 100px; width: 300px; height: 2px; background: var(--ink);
  }
  .holder {
    position: absolute; right: 22px; top: 108px; text-align: right; color: var(--ink);
  }
  .holder .name { font-weight: 700; font-size: 19px; line-height: 22px; }
  .holder .title { font-weight: 700; font-size: 14px; line-height: 17px; }
  .divider-right {
    position: absolute; right: 0; top: 152px; width: 120px; height: 2px; background: var(--ink);
  }

  .contacts {
    position: absolute; right: 22px; top: 164px;
    list-style: none; color: var(--ink); font-size: 13px;
  }
  .contacts li {
    display: flex; justify-content: flex-end; align-items: center; gap: 10px;
    height: 20px; white-space: nowrap;
  }
  .contacts .label { display: inline-block; width: 38px; text-align: left; }
  .icon {
    width: 14px; height: 14px; background: var(--ink); flex: none;
    display: flex; align-items: center; justify-content: center;
  }
  .icon svg { width: 10px; height: 10px; fill: var(--card); stroke: var(--card); }
</style>
</head>
<body>

<section class="card card--front" aria-label="Card front">
  <div class="front-brand">
    <span class="mark-square"></span>
    <span class="wordmark">BrivoPeak Partners</span>
  </div>
</section>

<section class="card card--back" aria-label="Card back">
  <div class="back-brand">
    <span class="mark-square"></span>
    <span class="wordmark">BrivoPeak Partners</span>
  </div>
  <div class="divider-left"></div>

  <div class="holder">
    <p class="name">Marlena Okafor</p>
    <p class="title">Managing Director</p>
  </div>
  <div class="divider-right"></div>

  <ul class="contacts">
    <li><span><span class="label">US:</span>(555) 214-0187</span>
      <span class="icon"><svg viewBox="0 0 10 10"><path stroke="none" d="M2 0h2l1 2.5-1.2 1a6 6 0 0 0 2.7 2.7l1-1.2L10 6v2a2 2 0 0 1-2 2A8 8 0 0 1 0 2a2 2 0 0 1 2-2z"/></svg></span></li>
    <li><span><span class="label">UK :</span>+44 7700 900412</span>
      <span class="icon"><svg viewBox="0 0 10 10"><path stroke="none" d="M2 0h2l1 2.5-1.2 1a6 6 0 0 0 2.7 2.7l1-1.2L10 6v2a2 2 0 0 1-2 2A8 8 0 0 1 0 2a2 2 0 0 1 2-2z"/></svg></span></li>
    <li><span>mokafor@brivopeakpartners.com</span>
      <span class="icon"><svg viewBox="0 0 10 10"><rect x="0.5" y="2" width="9" height="6" fill="none" stroke-width="1"/><path d="M0.5 2L5 5.5 9.5 2" fill="none" stroke-width="1"/></svg></span></li>
    <li><span>www.brivopeakpartners.com</span>
      <span class="icon"><svg viewBox="0 0 10 10"><circle cx="5" cy="5" r="4.3" fill="none" stroke-width="1"/><ellipse cx="5" cy="5" rx="2" ry="4.3" fill="none" stroke-width="0.8"/><path d="M0.7 5h8.6" stroke-width="0.8"/></svg></span></li>
    <li><span>14 Harrow Lane, London, E2 8QT, Great Britain</span>
      <span class="icon"><svg viewBox="0 0 10 10"><path stroke="none" d="M5 0a3.5 3.5 0 0 1 3.5 3.5C8.5 6 5 10 5 10S1.5 6 1.5 3.5A3.5 3.5 0 0 1 5 0zm0 2a1.5 1.5 0 1 0 0 3 1.5 1.5 0 0 0 0-3z"/></svg></span></li>
    <li><span>412 N Cedar Ave, Suite 210, Riverton UT 84065, United States</span>
      <span class="icon"><svg viewBox="0 0 10 10"><path stroke="none" d="M5 0a3.5 3.5 0 0 1 3.5 3.5C8.5 6 5 10 5 10S1.5 6 1.5 3.5A3.5 3.5 0 0 1 5 0zm0 2a1.5 1.5 0 1 0 0 3 1.5 1.5 0 0 0 0-3z"/></svg></span></li>
  </ul>
</section>

</body>
</html>
```